Elegant invitation for prestigious fund raising event

Background
The Lanterns of Grace is a very prestigious fund raising event. It is a sit down dinner, gala type evening with a presentation and auction.
There are three of these event being held at venues around western North Carolina. The areas where these are being held all have one thing in common, they are in the Appalachian Mountains and the craft of quilt making. As you will see from the Concept Boards attached why a mountain theme and quilt “design feel” is being used. One very important point - we don’t want this design to look like an actual quilt.

See the concept board on page 4, which we can’t use that is from another artist but is one good interpretation of the idea and one way to stylize the picture with a “quilt” interpretation and feel. We do not want a literal quilt representation but are looking for an artistic way on how best to interpret what the quilt represents - the feel of “stitching together” the different things across our region that make us all unique but yet bind us all as one.

The Brief:
We want to develop an elegant invitation for these events.
We have develop as save the date (attached) and all we want to use of this is the wording “Lanterns of Grace” we do not like the icon above it.
Also attached is the wording for the invitation, along with the new picture we want to use (taken from the inspiration boards)

Size, fold, color and paper:

Around 5x7 inches, but open to any dimension if you have an idea that will work in a totally different size. Ideally try and stick to something that will fit a standard envelope so that we don’t need to make a special envelope

Fold – up to you if it has a fold or not and which way it folds. Our thought is that it will need a fold to keep it up market but open to any suggestions.
We are happy to print this on a textured paper if you have suggestions. It will be professionally digital printed so the paper needs to be suitable for digital printing

Color. The inspiration boards show the color palette. We have started out in the save the dates with the navy with reversed out white but again totally up to you to use anything from that color palette.
Updates

Target Market(s)

Up market, around 50 - 65 years old, many are retired, very wealthy

Industry/Entity Type

Event

Requirements
Must have
• See brief attached
Nice to have
• See brief attached
Should not have
• See brief attached

```html
<!DOCTYPE html>
<html lang="en">
<head>
<meta charset="utf-8">
<title>Lanterns of Grace – Invitation</title>
<link rel="stylesheet" href="https://fonts.googleapis.com/css2?family=Arimo:ital,wght@1,400;1,700&family=Cormorant+SC:wght@600&family=Josefin+Sans:wght@300&family=Lobster&display=swap">
<style>
  :root {
    --page-bg: #eeeef0;
    --navy-deep: #1f3f86;
    --navy-mid: #3b6fc4;
    --sky-pale: #7fa3dc;
    --sunset-orange: #f2a24a;
    --sunset-gold: #f6c25c;
    --ridge-blue: #5c77b4;
    --forest-dark: #1f3a22;
    --forest-mid: #3f6a34;
    --ink-navy: #1d1a4f;
    --paper-white: #ffffff;
    --wash-violet: #a24aa8;
    --wash-magenta: #e2468f;
    --wash-rose: #f3a3ae;
    --wash-cream: #f8f1e4;
    --wash-peach: #f6c8a6;
  }
  html, body {
    margin: 0;
    padding: 0;
    width: 976px;
    height: 1200px;
    overflow: hidden;
    background: var(--page-bg);
  }
  .canvas {
    position: relative;
    width: 976px;
    height: 1200px;
  }

  /* Folded cover card */
  .cover-card {
    position: absolute;
    left: 40px;
    top: 40px;
    width: 580px;
    height: 760px;
    box-shadow: 0 6px 18px rgba(0,0,0,0.18);
    overflow: hidden;
  }
  .cover-back-panel {
    position: absolute;
    inset: 0 0 auto 0;
    height: 355px;
    background: radial-gradient(ellipse at 60% 40%, var(--sky-pale) 0%, var(--navy-mid) 45%, var(--navy-deep) 100%);
  }
  .cover-front-panel {
    position: absolute;
    left: 0; right: 0; bottom: 0;
    height: 405px;
    background: linear-gradient(180deg,
      var(--navy-mid) 0%,
      var(--sky-pale) 14%,
      var(--sunset-gold) 24%,
      var(--sunset-orange) 32%,
      var(--ridge-blue) 42%,
      var(--forest-mid) 62%,
      var(--forest-dark) 100%);
  }
  .fold-line {
    position: absolute;
    left: 0; right: 0;
    top: 355px;
    border-top: 1.5px dashed rgba(255,255,255,0.8);
  }
  .hospital-name {
    position: absolute;
    right: 60px;
    top: 78px;
    transform: rotate(180deg);
    display: flex;
    align-items: center;
    gap: 10px;
    color: var(--paper-white);
    font-family: "Cormorant SC", Georgia, serif;
    font-weight: 600;
  }
  .hospital-name .mark-square {
    width: 22px;
    height: 22px;
    background: var(--paper-white);
  }
  .hospital-name .name-lines {
    display: flex;
    flex-direction: column;
    align-items: center;
    line-height: 1.05;
  }
  .hospital-name .name-main { font-size: 23px; letter-spacing: 0.5px; }
  .hospital-name .name-sub { font-size: 14px; letter-spacing: 1px; }

  .event-name {
    position: absolute;
    left: 170px;
    top: 540px;
    width: 240px;
    display: flex;
    flex-direction: column;
    align-items: center;
    gap: 14px;
    color: var(--paper-white);
    font-family: "Josefin Sans", Arial, sans-serif;
    font-weight: 300;
  }
  .event-name .mark-circle {
    width: 54px;
    height: 54px;
    border-radius: 50%;
    background: var(--paper-white);
  }
  .event-name .name-text {
    font-size: 34px;
    line-height: 1.05;
    text-align: center;
    text-transform: uppercase;
    letter-spacing: 1px;
  }

  /* Invitation card */
  .invitation-card {
    position: absolute;
    left: 420px;
    top: 365px;
    width: 505px;
    height: 712px;
    box-shadow: 0 6px 18px rgba(0,0,0,0.2);
    overflow: hidden;
  }
  .watercolor-wash {
    position: absolute;
    inset: 0;
    background:
      radial-gradient(ellipse at 10% 4%, var(--wash-violet) 0%, transparent 38%),
      linear-gradient(180deg,
        var(--wash-magenta) 0%,
        var(--wash-rose) 24%,
        var(--wash-peach) 38%,
        var(--wash-cream) 50%,
        var(--wash-cream) 66%,
        var(--wash-rose) 78%,
        var(--wash-magenta) 92%,
        var(--wash-magenta) 100%);
  }
  .invitation-frame {
    position: absolute;
    inset: 14px;
    border: 1.5px solid var(--paper-white);
  }
  .invitation-title {
    position: absolute;
    left: 0; right: 0;
    top: 52px;
    text-align: center;
  }
  .invitation-title span {
    font-family: "Lobster", cursive;
    font-size: 26px;
    color: var(--paper-white);
    border-bottom: 2px solid var(--paper-white);
    padding: 0 3px 1px;
  }
  .invitation-copy {
    position: absolute;
    left: 30px; right: 30px;
    margin: 0;
    text-align: center;
    color: var(--ink-navy);
    font-family: "Arimo", Arial, sans-serif;
    font-style: italic;
  }
  .invitation-copy .line { display: block; }
  .invitation-intro {
    top: 118px;
    font-weight: 700;
    font-size: 14px;
    line-height: 37px;
  }
  .invitation-details {
    top: 408px;
    font-weight: 400;
    font-size: 14px;
    line-height: 36.5px;
    text-transform: uppercase;
  }
  .invitation-details sup { font-size: 8px; }
  .proceeds-note {
    position: absolute;
    left: 30px; right: 30px;
    top: 592px;
    margin: 0;
    text-align: center;
    color: var(--ink-navy);
    font-family: "Arimo", Arial, sans-serif;
    font-style: italic;
    font-size: 10px;
  }
</style>
</head>
<body>
<main class="canvas">

  <section class="cover-card" aria-label="Folded cover card">
    <div class="cover-back-panel" role="img" aria-label="Deep blue textured panel with swirling flourish pattern"></div>
    <div class="cover-front-panel" role="img" aria-label="Painted mountain landscape at sunset with forested ridges"></div>
    <div class="fold-line"></div>

    <div class="hospital-name">
      <div class="mark-square"></div>
      <div class="name-lines">
        <span class="name-main">Ridgeview Valley</span>
        <span class="name-sub">Hospital</span>
      </div>
    </div>

    <div class="event-name">
      <div class="mark-circle"></div>
      <div class="name-text">Lanterns of Grace</div>
    </div>
  </section>

  <section class="invitation-card" aria-label="Invitation card">
    <div class="watercolor-wash" role="img" aria-label="Violet, pink and cream watercolour wash"></div>
    <div class="invitation-frame"></div>

    <h1 class="invitation-title"><span>Invitation</span></h1>

    <p class="invitation-copy invitation-intro">
      <span class="line">You are invited to</span>
      <span class="line">The Second Annual</span>
      <span class="line">LANTERNS OF GRACE on the plateau.</span>
      <span class="line">Please join us for an elegant and entertaining affair</span>
      <span class="line">benefiting the healthcare in our region.</span>
    </p>

    <p class="invitation-copy invitation-details">
      <span class="line">6<sup>th</sup> of June, 2016</span>
      <span class="line">The Meadow at Laurel Crest Lodge</span>
      <span class="line">Beginning at 5:30pm</span>
      <span class="line">Valet Parking</span>
      <span class="line">Cocktail Attire &middot; Valet Parking</span>
    </p>

    <p class="proceeds-note">All Proceeds From The Night Will Go To Benefit Ridgeview Valley Hospital</p>
  </section>

</main>
</body>
</html>
```